RESIDENCE VALBRUNE

The CORVALE Immobilier company exclusively offers apartments for sale under a tax exemption law (BELTRAVIGNE) in CAMBRAI, 92 apartments are available, fully renovated with balcony, terrace, elevator, in a former military residence known to the city.
We want to make a book to give to our customers.

```html
<!DOCTYPE html>
<html lang="fr">
<head>
<meta charset="utf-8">
<title>Résidence Valbrune – Cambrai</title>
<link href="https://fonts.googleapis.com/css2?family=Montserrat:wght@800&family=Poppins:wght@300;400;500;600;700&display=swap" rel="stylesheet">
<style>
:root{
  --gold:#a57c4c;
  --ink:#1d1d1d;
  --blue:#5a7ca3;
  --paper:#ffffff;
  --line:#b08a5c;
}
*{margin:0;padding:0;box-sizing:border-box}
html,body{width:1200px;height:3172px;overflow:hidden;background:var(--paper)}
body{position:relative;font-family:"Poppins",sans-serif;color:var(--ink)}
.abs{position:absolute}
.frame{position:absolute;border:2px solid var(--line)}
.frame.thin{border-width:1.5px}
.visual{position:absolute}
.brand{position:absolute;text-align:center;color:var(--gold);font-family:"Poppins",sans-serif;font-weight:500;line-height:1}
.brand span{display:block}
.brand .word{font-size:22px;letter-spacing:.04em}
.brand .sub{font-size:8.5px;letter-spacing:.42em;margin-top:3px}
.body-copy{position:absolute;font-size:8.6px;line-height:1.45;font-weight:400}
.body-copy p+p{margin-top:10px}
.center{text-align:center}
.right{text-align:right}
.gold{color:var(--gold)}
/* cover */
.cover-title{position:absolute;left:488px;top:92px;height:560px;writing-mode:vertical-rl;transform:rotate(180deg);font-family:"Montserrat",sans-serif;font-weight:800;font-size:112px;color:#fff;letter-spacing:.01em;line-height:1;text-align:center}
.tagline{position:absolute;right:62px;top:746px;text-align:right;font-size:22px;letter-spacing:.34em;line-height:34px;font-weight:400}
.tagline .accent{color:var(--gold);font-weight:600}
/* page title */
.page-head{position:absolute;right:22px;top:1040px;text-align:right;font-size:21px;line-height:23px;font-weight:400}
.page-head .accent{color:var(--gold);font-weight:600}
.section-label{position:absolute;width:100%;text-align:center;font-weight:600;font-size:10.5px}
.bar{position:absolute;background:var(--gold)}
.vertical-up{position:absolute;writing-mode:vertical-rl;transform:rotate(180deg);font-weight:700;font-size:45px;line-height:1;white-space:nowrap}
.vertical-down{position:absolute;writing-mode:vertical-rl;font-weight:700;font-size:45px;line-height:1;white-space:nowrap;color:var(--gold)}
.contact{position:absolute;left:27px;width:1146px;top:2993px;text-align:center;font-size:18.5px;letter-spacing:.38em;line-height:26.5px;font-weight:500}
</style>
</head>
<body>

<!-- COVER -->
<section class="cover">
  <div class="frame" style="left:27px;top:27px;width:1146px;height:843px"></div>
  <div class="visual" role="img" aria-label="Photographie du beffroi de l'hôtel de ville de Cambrai sous un ciel bleu" style="left:54px;top:57px;width:524px;height:785px;background:linear-gradient(180deg,#4f6f98 0%,#7f98b6 35%,#b7ab94 60%,#8d7b62 100%)"></div>
  <div class="cover-title">CAMBRAI</div>
  <svg class="abs" style="left:0;top:0" width="1200" height="900" viewBox="0 0 1200 900">
    <defs>
      <linearGradient id="stone" x1="0" y1="0" x2="0" y2="1">
        <stop offset="0" stop-color="#6f8fb5"/><stop offset=".55" stop-color="#b9b4aa"/><stop offset="1" stop-color="#7b6a55"/>
      </linearGradient>
      <linearGradient id="column" x1="0" y1="0" x2="1" y2="1">
        <stop offset="0" stop-color="#8a7a63"/><stop offset=".5" stop-color="#4a3f33"/><stop offset="1" stop-color="#a8977c"/>
      </linearGradient>
    </defs>
    <polygon role="img" aria-label="Détail du dôme du beffroi" fill="url(#stone)" points="748,148 867.5,217 867.5,355 748,424 628.5,355 628.5,217"/>
    <polygon role="img" aria-label="Détail sombre du clocher" fill="#2c2a27" points="698,414 725.7,430 725.7,462 698,478 670.3,462 670.3,430"/>
    <polygon fill="var(--blue)" points="1019,327 1048.4,344 1048.4,378 1019,395 989.6,378 989.6,344"/>
    <polygon role="img" aria-label="Détail des colonnes du beffroi" fill="url(#column)" points="843,388 917.5,431 917.5,517 843,560 768.5,517 768.5,431"/>
    <polygon role="img" aria-label="Détail d'une colonne en pierre" fill="url(#column)" points="985,394 1050.8,432 1050.8,508 985,546 919.2,508 919.2,432"/>
    <polygon role="img" aria-label="Détail de la cloche et des automates" fill="url(#column)" points="911,515 976.8,553 976.8,629 911,667 845.2,629 845.2,553"/>
    <polygon fill="var(--blue)" points="1055,508 1124.3,548 1124.3,628 1055,668 985.7,628 985.7,548"/>
  </svg>
  <div class="brand" style="right:62px;top:128px"><span class="word" style="font-size:30px">CORVALE</span><span class="sub" style="font-size:11px">IMMOBILIER</span></div>
  <div class="tagline">
    <div>LA RÉSIDENCE VALBRUNE</div>
    <div>À CAMBRAI DEVIENT</div>
    <div class="accent">LA RÉSIDENCE ALTAIR</div>
  </div>
</section>

<!-- PAGE : CAMBRAI -->
<section>
  <div class="frame thin" style="left:12px;top:917px;width:575px;height:425px"></div>
  <div class="visual" role="img" aria-label="Carte de France situant Cambrai" style="left:252px;top:926px;width:95px;height:92px;background:linear-gradient(135deg,#f1f1f1,#e2e2e2)"></div>
  <div class="brand" style="left:485px;top:972px"><span class="word">CORVALE</span><span class="sub">IMMOBILIER</span></div>
  <div class="section-label" style="left:12px;width:575px;top:1030px">CAMBRAI</div>
  <div class="body-copy center" style="left:34px;top:1052px;width:531px">
    <p>Est une commune française, historiquement capitale du Cambrésis, située dans le département du Nord, dont elle est aujourd'hui l'une des sous-préfectures, en région Hauts-de-France. Cambrai est une ville moyenne de plus de trente mille habitants, au cœur d'une unité urbaine de près de cinquante mille habitants. Son aire d'attraction, plus étendue, rassemble près de cent mille habitants. Avec Lille et les villes de l'ancien bassin minier, elle participe aussi à un vaste ensemble métropolitain.</p>
    <p>Vers la fin de l'Empire romain, Cambrai remplace Bavay comme capitale de la cité des Nerviens. Au début de l'époque mérovingienne, elle devient le siège d'un vaste évêché s'étendant sur la rive droite de l'Escaut, puis le centre d'une petite principauté ecclésiastique rattachée à la France au XVIIᵉ siècle.</p>
    <p>Les terres fertiles qui l'entourent et l'industrie textile font sa prospérité du Moyen Âge à l'époque moderne. Occupée et partiellement détruite pendant la Première Guerre mondiale, Cambrai voit se dérouler à ses portes une bataille restée célèbre. La Seconde Guerre mondiale est suivie de reconstructions et d'un rapide développement économique et démographique.</p>
    <p>De son passé historique mouvementé, cette ville conserve un cadre de vie agréable et un riche patrimoine monumental. Cambrai s'est affirmée comme le centre urbain du Cambrésis. Cité aux fonctions locales diversifiées, elle développe à nouveau son économie, notamment dans la logistique et grâce à son futur port intérieur connecté au canal Seine-Nord Europe, lié à sa position stratégique au centre du nord de l'Europe.</p>
  </div>
</section>

<!-- PAGE : ANNONCE -->
<section>
  <div class="frame thin" style="left:613px;top:917px;width:573px;height:425px"></div>
  <div class="visual" role="img" aria-label="Aperçu miniature d'une plaquette avec plans" style="left:642px;top:944px;width:101px;height:73px;background:linear-gradient(135deg,#f4efe8,#d9cdbd);border:1px solid #444"></div>
  <div class="brand" style="right:26px;top:972px"><span class="word">CORVALE</span><span class="sub">IMMOBILIER</span></div>
  <svg class="abs" style="left:613px;top:940px" width="400" height="380" viewBox="613 940 400 380">
    <defs>
      <linearGradient id="render1" x1="0" y1="0" x2="0" y2="1">
        <stop offset="0" stop-color="#a9c4e0"/><stop offset=".45" stop-color="#b8624a"/><stop offset=".8" stop-color="#8d8f8a"/><stop offset="1" stop-color="#6f8a5a"/>
      </linearGradient>
    </defs>
    <polygon role="img" aria-label="Perspective 3D de la résidence rénovée en briques rouges" fill="url(#render1)" points="613,1068 982,962 982,1188 613,1290"/>
    <line x1="887" y1="975" x2="982" y2="948" stroke="var(--gold)" stroke-width="5"/>
    <line x1="902" y1="985" x2="982" y2="962" stroke="var(--gold)" stroke-width="5"/>
    <line x1="625" y1="1292" x2="725" y2="1264" stroke="var(--gold)" stroke-width="5"/>
    <line x1="625" y1="1303" x2="725" y2="1275" stroke="var(--gold)" stroke-width="5"/>
  </svg>
  <div class="page-head">
    <div>LA</div><div>RÉSIDENCE</div><div>VALBRUNE</div><div>À CAMBRAI</div><div>DEVIENT</div>
    <div class="accent">LA RÉSIDENCE</div><div class="accent">ALTAIR</div>
  </div>
  <div class="body-copy right" style="left:720px;top:1270px;width:444px">Le GROUPE CORVALE Immobilier vous propose de réaliser un investissement locatif en BELTRAVIGNE ; le spécialiste de l'investissement locatif clefs en main se lance dans un programme immobilier ambitieux, à l'issue de son succès avec la rénovation d'une ancienne caserne militaire à Cambrai. Éligible au dispositif, cette opération offre une opportunité unique aux primo-investisseurs.</div>
</section>

<!-- SPREAD : PROJET -->
<section>
  <div class="frame thin" style="left:12px;top:1375px;width:1174px;height:422px"></div>
  <div class="bar" style="left:37px;top:1392px;width:7px;height:60px"></div>
  <div class="bar" style="left:47px;top:1404px;width:7px;height:68px"></div>
  <div class="bar" style="left:57px;top:1418px;width:7px;height:90px"></div>
  <div class="body-copy" style="left:70px;top:1437px;width:246px">
    <p>L'ancienne résidence militaire « Valbrune » va faire peau neuve et se transformer en résidence de standing ! Souhaitant conserver l'historique des lieux, elle portera le nom d'ALTAIR. Les 3 bâtiments seront baptisés en souvenir de l'armée française.</p>
    <p>Cette résidence construite en 1958, située à deux pas du centre-ville et du quartier Saint-Roch, est en pleine rénovation. 92 logements de standing y sont proposés à partir de 125 000 euros, les premiers seront livrés en 2023 ! C'est un projet titanesque, dont le promoteur lillois s'est lancé comme défi de rénover l'ensemble, les parties communes, les façades extérieures, les toitures et les espaces communs.</p>
    <p>Les 3 bâtiments seront habitables d'ici la fin de l'année 2025, et le premier bâtiment baptisé « Zénith » sera le premier à héberger les premiers locataires ou propriétaires.</p>
  </div>
  <div class="visual" role="img" aria-label="Perspective 3D de la façade rénovée avec balcons, rue et voitures" style="left:347px;top:1442px;width:506px;height:284px;background:linear-gradient(180deg,#e9eef2 0%,#c06b4f 22%,#b65e45 60%,#7d8a5c 78%,#6e6e6c 100%)"></div>
  <div class="brand" style="right:24px;top:1430px"><span class="word">CORVALE</span><span class="sub">IMMOBILIER</span></div>
  <div class="body-copy right" style="left:868px;top:1477px;width:252px">
    <p style="font-weight:600">Le promoteur a choisi d'allier LE GROUPE CORVALE Immobilier à sa cause</p>
    <p>Reconnu pour son savoir-faire en matière d'investissement locatif à Cambrai, LE GROUPE CORVALE IMMOBILIER se lance en co-promotion et la commercialisation exclusive d'un nouveau projet : la rénovation d'une ancienne résidence militaire. « Les bâtiments ont été très bien conçus, ce qui nous offre la possibilité de réaliser des produits de qualité avec des ascenseurs, des balcons, des rez-de-jardin, des caves et même quelques places de parking » détaille Marc Duval. Chargé du développement du groupe immobilier « La résidence est éligible au dispositif BELTRAVIGNE, CAMBRAI est l'une des villes exclusives à bénéficier de cette aide fiscale. C'est une véritable opportunité puisque le dispositif doit s'achever le 31 décembre 2022 et que nous ne</p>
  </div>
  <div class="bar" style="left:1139px;top:1661px;width:7px;height:90px"></div>
  <div class="bar" style="left:1149px;top:1690px;width:7px;height:68px"></div>
  <div class="bar" style="left:1159px;top:1712px;width:7px;height:66px"></div>
</section>

<!-- SPREAD : OPPORTUNITÉ -->
<section>
  <div class="visual" role="img" aria-label="Perspective 3D de la rue bordée par la résidence en briques" style="left:0;top:1815px;width:435px;height:243px;background:linear-gradient(160deg,#dfe8ee 0%,#b86a50 35%,#9aa08c 65%,#7c8f5a 100%)"></div>
  <div class="visual" role="img" aria-label="Perspective 3D d'une entrée de bâtiment" style="left:347px;top:2025px;width:163px;height:90px;background:linear-gradient(135deg,#e7ecef 0%,#bf6c50 55%,#7f935e 100%)"></div>
  <div class="body-copy right" style="left:70px;top:2142px;width:367px">Le dispositif BELTRAVIGNE offre la possibilité aux particuliers acquéreurs d'un appartement ancien dans un but locatif de bénéficier d'une réduction d'impôt sur le revenu pouvant aller jusqu'à 6 000 euros par an. Seule contrainte : louer le logement non meublé comme résidence principale pendant 6, 9 ou 12 ans. « Nous proposons une opération clé en main puisque c'est le promoteur qui réalise les travaux de rénovation et que nous pouvons accompagner les investisseurs dans le financement de leur bien mais aussi assurer la gestion locative de celui-ci » explique Marc Duval.</div>
  <div class="vertical-up" style="left:554px;top:1846px;height:384px;text-align:center">UNE VÉRITABLE</div>
  <div class="vertical-down" style="left:603px;top:1840px;height:390px;text-align:center">OPPORTUNITÉ !</div>
  <div class="body-copy" style="left:763px;top:1846px;width:365px;line-height:1.3">
    <p>Ce programme est une occasion inédite pour les primo-investisseurs de se constituer un premier patrimoine immobilier. « Grâce à nos partenaires financiers, il est possible d'acquérir un logement dans cette résidence sans apport et de le faire financer entièrement grâce au loyer perçu » ajoute-t-il, rappelant que LE GROUPE CORVALE propose une assurance 100 % garantie loyer impayé, sans délais de carence et en paiement immédiat. « L'immobilier demeure un investissement de choix, c'est une valeur sûre et il est possible de revendre son bien à tout moment » souligne Marc Duval.</p>
    <p>LE GROUPE CORVALE Immobilier est à votre disposition pour vous recevoir et vous fournir toutes les informations sur cette nouvelle résidence et vous établir une étude fiscale personnalisée, pour optimiser votre investissement locatif.</p>
    <p style="font-weight:600">Pour toute réservation d'un logement d'ici le<br>30 juin, les frais de notaire sont offerts !</p>
  </div>
  <div class="visual" role="img" aria-label="Perspective 3D d'une cage d'escalier et façade en briques" style="left:763px;top:2019px;width:437px;height:246px;background:linear-gradient(120deg,#e8edf0 0%,#d9d7d2 30%,#b4634a 55%,#a75a43 80%,#6f8457 100%)"></div>
</section>

<!-- BACK COVER -->
<section>
  <div class="frame" style="left:27px;top:2299px;width:1146px;height:843px"></div>
  <div class="brand" style="left:27px;width:1146px;top:2752px"><span class="word" style="font-size:62px">CORVALE</span><span class="sub" style="font-size:22px;margin-top:10px">IMMOBILIER</span></div>
  <div class="contact">
    <div>GROUPE CORVALE IMMOBILIER</div>
    <div>14 RUE DES TILLEULS</div>
    <div>59400 CAMBRAI</div>
    <div>01 23 45 67 89</div>
  </div>
</section>

</body>
</html>
```